Business Card

We need a business card for a fundraising/sales and marketing company called Kelvora Appeals services. The logo colours are Red Black and white. The final design should communicate professional, reliable yet fun and charity minded
Updates

Sorry for the delay. A decision will be made in the next 48 hours. we are stuck between two designs. Kind Regards, Molly Ravenscroft

Industry/Entity Type

Marketing

```html
<!DOCTYPE html>
<html lang="en">
<head>
<meta charset="utf-8">
<title>Kelvora Appeals services – Business Card</title>
<link rel="stylesheet" href="https://fonts.googleapis.com/css2?family=Alegreya+Sans:wght@400;500&display=swap">
<style>
  :root {
    --stage: #1c1c1c;
    --red: #d71920;
    --red-deep: #a50f14;
    --band-light: #ffffff;
    --band-edge: #d6d6d6;
    --ink-logo: #3a3a3a;
    --ink-light: #dcdcdc;
    --icon-bg: #d9d9d9;
    --icon-ink: #b3141a;
  }
  html, body {
    margin: 0;
    width: 1200px;
    height: 900px;
    overflow: hidden;
    background: var(--stage);
    font-family: "Alegreya Sans", sans-serif;
  }
  .card {
    position: absolute;
    left: 100px;
    top: 164px;
    width: 1000px;
    height: 572px;
    overflow: hidden;
    background: radial-gradient(ellipse at 45% 45%, var(--red) 0%, var(--red) 45%, var(--red-deep) 100%);
  }
  .rule {
    position: absolute;
    left: 0;
    width: 100%;
    height: 3px;
    background: var(--band-light);
    opacity: .85;
  }
  .rule--top { top: 52px; }
  .rule--bottom { top: 278px; }
  .brand-band {
    position: absolute;
    left: 0;
    top: 64px;
    width: 100%;
    height: 202px;
    background: radial-gradient(ellipse at 50% 50%, var(--band-light) 0%, #f1f1f1 55%, var(--band-edge) 100%);
  }
  .brand {
    position: absolute;
    left: 50%;
    top: 50%;
    transform: translate(-50%, -50%);
    display: flex;
    align-items: center;
    gap: 14px;
  }
  .brand__dot {
    width: 22px;
    height: 22px;
    border-radius: 50%;
    background: var(--red);
  }
  .brand__name {
    font-size: 44px;
    font-weight: 500;
    letter-spacing: 2px;
    color: var(--ink-logo);
    text-transform: uppercase;
  }
  .holder {
    position: absolute;
    left: 72px;
    top: 430px;
    color: var(--ink-light);
  }
  .holder__name {
    font-size: 46px;
    font-weight: 500;
    letter-spacing: 1px;
    margin: 0;
    line-height: 1;
  }
  .holder__title {
    font-size: 28px;
    margin: 8px 0 0;
  }
  .divider {
    position: absolute;
    left: 528px;
    top: 310px;
    width: 2px;
    height: 200px;
    background: linear-gradient(to bottom, transparent, #8a6f6f 20%, #8a6f6f 80%, transparent);
  }
  .contacts {
    position: absolute;
    left: 572px;
    top: 318px;
    margin: 0;
    padding: 0;
    list-style: none;
  }
  .contacts__item {
    display: flex;
    align-items: center;
    gap: 14px;
    height: 52px;
    color: var(--ink-light);
    font-size: 24px;
  }
  .contacts__icon {
    width: 32px;
    height: 32px;
    flex: none;
  }
</style>
</head>
<body>
  <article class="card">
    <div class="rule rule--top"></div>
    <section class="brand-band">
      <div class="brand">
        <span class="brand__dot"></span>
        <span class="brand__name">Kelvora Appeals</span>
      </div>
    </section>
    <div class="rule rule--bottom"></div>

    <div class="holder">
      <p class="holder__name">Declan Harrowgate</p>
      <p class="holder__title">Managing Director</p>
    </div>

    <div class="divider"></div>

    <ul class="contacts">
      <li class="contacts__item">
        <svg class="contacts__icon" viewBox="0 0 32 32" aria-hidden="true">
          <circle cx="16" cy="16" r="16" fill="var(--icon-bg)"/>
          <path d="M8 13c0-3 4-4 8-4s8 1 8 4v2h-4v-2h-8v2H8z" fill="var(--icon-ink)"/>
          <rect x="10" y="16" width="12" height="7" rx="1.5" fill="var(--icon-ink)"/>
        </svg>
        <span>0400-555-017</span>
      </li>
      <li class="contacts__item">
        <svg class="contacts__icon" viewBox="0 0 32 32" aria-hidden="true">
          <circle cx="16" cy="16" r="16" fill="var(--icon-bg)"/>
          <rect x="8" y="10" width="16" height="12" rx="1" fill="var(--icon-ink)"/>
          <path d="M8.5 10.5 16 17l7.5-6.5" fill="none" stroke="var(--icon-bg)" stroke-width="1.5"/>
        </svg>
        <span>declan@kelvoraappeals.com</span>
      </li>
      <li class="contacts__item">
        <svg class="contacts__icon" viewBox="0 0 32 32" aria-hidden="true">
          <circle cx="16" cy="16" r="16" fill="var(--icon-bg)"/>
          <circle cx="14" cy="14" r="6.5" fill="none" stroke="var(--icon-ink)" stroke-width="1.6"/>
          <path d="M7.5 14h13M14 7.5c-3 3.5-3 9.5 0 13M14 7.5c3 3.5 3 9.5 0 13" fill="none" stroke="var(--icon-ink)" stroke-width="1.2"/>
          <path d="M19 19l5 5" stroke="var(--icon-ink)" stroke-width="2.4" stroke-linecap="round"/>
        </svg>
        <span>www.kelvoraappeals.com</span>
      </li>
    </ul>
  </article>
</body>
</html>
```